Business Card Design Project

- makeup artist business card

- original and creative

- Elegant design

- Feel free to come out with cool designs but stick to being elegant and attractive

- Design relates to makeup

- includes name, occupation, contact numbers, email, website

- regular size business card

- round corner card

- double sided

- on 1 side it should just have the website name in the center " browsandblush.example "

Industry/Entity Type

Business

Requirements
Must have
• Marla Voss
Makeup Artist
USA: +1 (415)872-6410
Singapore: +65 83027715
marlavoss@browsandblush.example
www.browsandblush.example
Should not have
• nothing cartoon looking.
Pictures of makeup being grab from the internet.. Examples: eyes or lips.

```html
<!DOCTYPE html>
<html lang="en">
<head>
<meta charset="utf-8">
<title>Marla Voss – Makeup Artist</title>
<link rel="stylesheet" href="https://fonts.googleapis.com/css2?family=Cormorant+Garamond:wght@500&family=Source+Sans+3:wght@400&display=swap">
<style>
  :root {
    --paper: #ffffff;
    --magenta: #e21fb4;
    --band: #d93ee6;
    --ink-grey: #555a5f;
    --powder-pink: #f0559e;
    --powder-green: #93e83a;
    --powder-yellow: #eef04a;
    --powder-blue: #2c57c9;
    --powder-violet: #9b5be0;
    --lip-pink: #f28ab8;
  }
  html, body {
    margin: 0;
    padding: 0;
    width: 1200px;
    height: 686px;
    overflow: hidden;
    background: var(--paper);
  }
  .card {
    position: relative;
    width: 1200px;
    height: 686px;
    background: var(--paper);
    overflow: hidden;
  }
  .top-band {
    position: absolute;
    left: 0;
    top: 0;
    width: 100%;
    height: 11px;
    background: var(--band);
  }
  .powder-art {
    position: absolute;
    left: 0;
    top: 50px;
    width: 650px;
    height: 636px;
    background:
      radial-gradient(ellipse 110px 90px at 290px 110px, var(--powder-pink) 0%, rgba(240,85,158,0) 100%),
      radial-gradient(ellipse 170px 130px at 130px 200px, var(--powder-green) 0%, rgba(147,232,58,0) 100%),
      radial-gradient(ellipse 150px 120px at 340px 320px, var(--powder-yellow) 0%, rgba(238,240,74,0) 100%),
      radial-gradient(ellipse 80px 60px at 190px 330px, var(--powder-violet) 0%, rgba(155,91,224,0) 100%),
      radial-gradient(ellipse 90px 70px at 330px 490px, var(--powder-blue) 0%, rgba(44,87,201,0) 100%),
      radial-gradient(ellipse 160px 110px at 470px 560px, var(--powder-pink) 0%, rgba(240,85,158,0) 100%),
      radial-gradient(ellipse 110px 90px at 110px 560px, #4fc25a 0%, rgba(79,194,90,0) 100%);
  }
  .lip-art {
    position: absolute;
    left: 940px;
    top: 480px;
    width: 260px;
    height: 206px;
    background: radial-gradient(ellipse 130px 90px at 130px 110px, var(--lip-pink) 0%, rgba(242,138,184,0.4) 60%, rgba(242,138,184,0) 100%);
  }
  .contact {
    position: absolute;
    left: 632px;
    top: 118px;
  }
  .contact__name {
    margin: 0 0 6px;
    font-family: "Cormorant Garamond", serif;
    font-weight: 500;
    font-size: 66px;
    line-height: 72px;
    color: var(--magenta);
    letter-spacing: -0.5px;
  }
  .contact__line {
    margin: 0;
    font-family: "Source Sans 3", sans-serif;
    font-size: 34px;
    line-height: 46px;
    color: var(--ink-grey);
    white-space: nowrap;
  }
</style>
</head>
<body>
  <div class="card">
    <div class="top-band"></div>
    <div class="powder-art" role="img" aria-label="Photograph of crushed, colourful eyeshadow powders in pink, green, yellow, violet and blue with an open jar of green pigment"></div>
    <div class="lip-art" role="img" aria-label="Pink lipstick kiss print"></div>
    <div class="contact">
      <h1 class="contact__name">Marla Voss</h1>
      <p class="contact__line">Makeup Artist</p>
      <p class="contact__line">USA: +1 (415)872-6410</p>
      <p class="contact__line">Singapore: +65 83027715</p>
      <p class="contact__line">marlavoss@browsandblush.example</p>
    </div>
  </div>
</body>
</html>
```